Attractive door board for entrance beautysalon

Make an attractive design for a board that can be glued on the front door of a beauty salon. The salon location has no window in the front so I need something catchy and attractive. The door board contains a list of the services and the website: www.atelierkm.be, and the text "Enkel op afspraak, bel 0486317492"

Target Market(s)

woman between 16 and 99 years old

Industry/Entity Type

Beauty Salon

Font styles to use
Sans Serif

Requirements
Must have
• A very nice, attractive but sober design.
• It must have a classy Morvane, Lusa, ... chique design.
• The logo must be on it (in attachment)
• There must be the following list in it:
• Gelaatsverzorging
• Wimperverlenging
• Wimperlifting
• Suikerontharing
• Permanente Make Up
• Airbrush Tanning
• Manicure - Pedicure - Velura
• and then the website www.atelierkm.be, and the text "Enkel op afspraak, bel 0486317492"
Nice to have
• a catchy design,
• max. width can be 75 cm and max height 180 cm as it is a design for a board that will be glued on a door.
Should not have
• orchid flowers, buddha look a likes

```html
<!DOCTYPE html>
<html lang="nl">
<head>
<meta charset="utf-8">
<title>Atelier KM – deurbord</title>
<link href="https://fonts.googleapis.com/css2?family=Bebas+Neue&family=Josefin+Sans:wght@300&family=Oswald:wght@300;500&display=swap" rel="stylesheet">
<style>
  :root {
    --ink: #231f20;
    --teal: #3a8aa6;
    --paper: #ffffff;
    --stage: #ffffff;
  }
  * { margin: 0; padding: 0; box-sizing: border-box; }
  html, body {
    width: 1200px; height: 1200px; overflow: hidden;
    background: var(--stage);
  }
  .door-board {
    position: absolute;
    left: 365px; top: 36px;
    width: 470px; height: 1128px;
    background: var(--ink);
    overflow: hidden;
  }
  .brand {
    position: absolute; left: 0; right: 0; top: 0; height: 366px;
    text-align: center; color: var(--paper);
  }
  .brand-name {
    position: absolute; left: 0; right: 0; top: 188px;
    font-family: "Josefin Sans", sans-serif; font-weight: 300;
    font-size: 34px; letter-spacing: 0.55em; padding-left: 0.55em;
  }
  .brand-tagline {
    position: absolute; left: 0; right: 0; top: 256px;
    font-family: "Josefin Sans", sans-serif; font-weight: 300;
    font-size: 10px; letter-spacing: 1.05em; padding-left: 1.05em;
  }
  .services {
    position: absolute; left: 0; right: 0; top: 366px;
    list-style: none;
    border-top: 10px solid var(--teal);
  }
  .service {
    height: 66px;
    border-bottom: 9px solid var(--teal);
    color: var(--paper);
    font-family: "Bebas Neue", sans-serif;
    font-size: 37px; letter-spacing: 0.02em;
    line-height: 57px;
    padding-left: 30px;
  }
  .service:last-child { border-bottom: none; height: 57px; }
  .service .dot { margin-right: 10px; }
  .appointment {
    position: absolute; left: 0; right: 0; top: 829px; height: 210px;
    background: var(--paper);
    border-bottom: 2px solid var(--teal);
  }
  .appointment-art {
    position: absolute; left: 0; top: 6px; width: 142px; height: 200px;
  }
  .appointment-text {
    position: absolute; left: 184px; top: 60px;
    color: var(--ink);
  }
  .appointment-note {
    font-family: "Oswald", sans-serif; font-weight: 300;
    font-size: 29px; letter-spacing: 0.02em; line-height: 42px;
  }
  .appointment-phone {
    font-family: "Oswald", sans-serif; font-weight: 500;
    font-size: 28px; letter-spacing: 0.03em; line-height: 42px;
  }
  .website {
    position: absolute; left: 0; right: 0; top: 1041px; height: 56px;
    color: var(--paper); text-align: center;
    font-family: "Oswald", sans-serif; font-weight: 500;
    font-size: 30px; line-height: 56px;
    letter-spacing: 0.22em; padding-left: 0.22em;
  }
  .footer-band {
    position: absolute; left: 0; right: 0; bottom: 0; height: 31px;
    background: var(--teal);
  }
</style>
</head>
<body>
  <main class="door-board">
    <header class="brand">
      <div class="brand-name">ATELIER KM</div>
      <div class="brand-tagline">SCHOONHEIDSINSTITUUT</div>
    </header>

    <ul class="services">
      <li class="service"><span class="dot">•</span>Gelaatsverzorging</li>
      <li class="service"><span class="dot">•</span>Wimperverlenging</li>
      <li class="service"><span class="dot">•</span>Wimperlifting</li>
      <li class="service"><span class="dot">•</span>Suikerontharing</li>
      <li class="service"><span class="dot">•</span>Permanente Make Up</li>
      <li class="service"><span class="dot">•</span>Airbrush Tanning</li>
      <li class="service"><span class="dot">•</span>Manicure <span class="dot" style="margin-left:6px">•</span>Pedicure <span class="dot" style="margin-left:6px">•</span>Velura</li>
    </ul>

    <section class="appointment">
      <svg class="appointment-art" role="img" aria-label="Watercolour illustration of an eye with lashes and colourful paint drips" viewBox="0 0 142 200" preserveAspectRatio="none">
        <defs>
          <linearGradient id="wash" x1="0" y1="0" x2="1" y2="1">
            <stop offset="0" stop-color="#e9d98a"/>
            <stop offset="0.35" stop-color="#b9c6dc"/>
            <stop offset="0.6" stop-color="#6f8fb0"/>
            <stop offset="1" stop-color="#d9c4e0"/>
          </linearGradient>
        </defs>
        <rect width="142" height="200" fill="url(#wash)" opacity="0.75"/>
      </svg>
      <div class="appointment-text">
        <div class="appointment-note">ENKEL OP AFSPRAAK</div>
        <div class="appointment-phone">BEL 0486317492</div>
      </div>
    </section>

    <div class="website">WWW.ATELIERKM.BE</div>
    <div class="footer-band"></div>
  </main>
</body>
</html>
```